Need a new company business card

I am looking for a new company business card. Front and back. With information on it as per below. Card should be professional. Yet clever. Simple. Modern design. TUV card, traditional size. OK with say, all black or all red backside.

VorraKay is an indie, bootstrapped magazine advancing the work of intersectional feminists busting their buts to create a just world through the power of enterprise and innovation.

VorraKay is the home and voice of entrepreneurial feminism and feminist innovators worldwide. Entrepreneurial feminists are people (of all genders) who see inequality as an innovation priority. They work to advance gender equity and/or who strive to integrate and practice feminist principles, pedagogy, values into their innovation and entrepreneurship work.
We are committed to this space being trans and queer inclusive, anti-racist, intersectional, brave, and safe. We welcome all allies. We value learning, edgy but civil discourse and integrative thinking skills.

Target Market(s)

feminists, business owners,

Industry/Entity Type

Publishing Company

Contact Information for Business Card

RD Halvorn
Founder/Publisher
2-340 Pellingham Street, Toronto, ON
M4T 2K8
publisher@vorrakay.com
416-555-0143
www.vorrakay.com

Font styles to use
Serif
Other font styles liked:
• Myriad Pro

Colors
ec1f27
000000
ffffff

Requirements
Must have
• logo
• use red, black white colours only.
Nice to have
• use the compass in pattern or creatively but not too busy please
Should not have
• Should not be too busy. Elegant.

```html
<!DOCTYPE html>
<html lang="en">
<head>
<meta charset="utf-8">
<title>VorraKay business card</title>
<link rel="stylesheet" href="https://fonts.googleapis.com/css2?family=Montserrat:wght@400;500;700;800&display=swap">
<style>
  :root {
    --red: #ec1f27;
    --black: #2b2b2b;
    --ink: #1e1e1e;
    --paper: #eeeeec;
    --silver-light: #dcdcdc;
    --silver-dark: #a9a9a9;
    --backdrop: #cdd3d3;
  }
  * { margin: 0; padding: 0; box-sizing: border-box; }
  html, body { width: 1200px; height: 1050px; overflow: hidden; }
  body {
    background: var(--backdrop);
    font-family: "Montserrat", Arial, sans-serif;
    display: flex;
    flex-direction: column;
    align-items: center;
    justify-content: center;
    gap: 40px;
  }
  .card {
    width: 800px;
    height: 457px;
    position: relative;
    overflow: hidden;
    box-shadow: 0 14px 30px rgba(0,0,0,0.18);
  }
  /* Front */
  .card-front {
    background: var(--paper);
    border-bottom: 5px solid var(--red);
  }
  .foil {
    position: absolute;
    left: 0; top: 0;
    width: 250px; height: 100%;
    background: linear-gradient(160deg, var(--silver-light) 0%, #c4c4c4 50%, var(--silver-dark) 100%);
  }
  .person {
    position: absolute;
    left: 290px; top: 170px;
  }
  .person-name {
    color: var(--red);
    font-weight: 700;
    font-size: 30px;
    line-height: 1.1;
  }
  .person-title {
    color: var(--ink);
    font-weight: 400;
    font-size: 18px;
    margin-top: 2px;
  }
  .brand {
    position: absolute;
    left: 500px; top: 120px;
    display: flex;
    align-items: flex-start;
    gap: 10px;
  }
  .brand-name {
    color: var(--ink);
    font-weight: 800;
    font-size: 46px;
    letter-spacing: -0.5px;
    line-height: 1;
  }
  .brand-dot {
    width: 14px; height: 14px;
    border: 1.5px solid var(--ink);
    border-radius: 50%;
    margin-top: 6px;
  }
  .contact {
    position: absolute;
    left: 500px; top: 200px;
    color: var(--ink);
    font-size: 16px;
    line-height: 1.45;
  }
  .address { margin-bottom: 16px; }
  .contact-list { list-style: none; }
  .contact-list li { display: flex; align-items: center; gap: 10px; }
  .contact-list svg { width: 15px; height: 15px; flex: none; }
  /* Back */
  .card-back {
    background: var(--black);
    border-bottom: 6px solid var(--red);
    display: flex;
    align-items: center;
    justify-content: center;
    gap: 22px;
  }
  .back-mark {
    width: 70px; height: 70px;
    border-radius: 50%;
    background: var(--red);
  }
  .back-name {
    color: #ffffff;
    font-weight: 800;
    font-size: 84px;
    letter-spacing: -1px;
  }
</style>
</head>
<body>
  <section class="card card-front">
    <div class="foil" role="img" aria-label="Silver foil decorative area"></div>
    <div class="person">
      <p class="person-name">RD Halvorn</p>
      <p class="person-title">Founder/Publisher</p>
    </div>
    <div class="brand">
      <span class="brand-name">VorraKay</span>
      <span class="brand-dot"></span>
    </div>
    <div class="contact">
      <p class="address">2-340 Pellingham Street<br>Toronto, ON, M4T 2K8</p>
      <ul class="contact-list">
        <li>
          <svg viewBox="0 0 16 16" aria-hidden="true"><path d="M4 1.5l2.2 3-1.3 1.6c.9 2 2.5 3.6 4.5 4.5l1.6-1.3 3 2.2-1.2 2.5C7 13.6 2.4 9 1.5 3z" fill="none" stroke="#ec1f27" stroke-width="1.5" stroke-linejoin="round"/></svg>
          416-555-0143
        </li>
        <li>
          <svg viewBox="0 0 16 16" aria-hidden="true"><rect x="1.5" y="3.5" width="13" height="9" fill="none" stroke="#ec1f27" stroke-width="1.5"/><path d="M1.5 3.5L8 9l6.5-5.5" fill="none" stroke="#ec1f27" stroke-width="1.5"/></svg>
          publisher@vorrakay.com
        </li>
        <li>
          <svg viewBox="0 0 16 16" aria-hidden="true"><circle cx="8" cy="8" r="6.5" fill="none" stroke="#ec1f27" stroke-width="1.4"/><ellipse cx="8" cy="8" rx="2.8" ry="6.5" fill="none" stroke="#ec1f27" stroke-width="1.2"/><path d="M1.5 8h13M2.5 5h11M2.5 11h11" stroke="#ec1f27" stroke-width="1.1"/></svg>
          www.vorrakay.com
        </li>
      </ul>
    </div>
  </section>

  <section class="card card-back">
    <span class="back-mark"></span>
    <span class="back-name">VorraKay</span>
  </section>
</body>
</html>
```